Quorvane Consulting

We focus on Data Recovery but we also do Network Security. We recover data from all types of hard drive form factors 3.5", 2.5", 1", 1.8", 5.25", 8" with any kind of interface IDE(PATA), SATA, mSATA, SCSI, SAS and Fibre Channel. All RAID Arrays 0, 1, 2, 3, 4, 5, 10 including nested levels like RAID 0+1, 1+0, 100, 0+3, 50 and 60, flash drives, like tablets, cellphones, usb drives, memory cards(SD, miniSD, Memory Stick(hovaku))

Actually you can gather any information or text from any data recovery site, cause is usually the same info, we would probably change a couple of things from the description so it wont look the same. One thing though, we want to make clear to users not to attempt data recovery themselves and to ship the faulty device to us, maybe we can illustrate this?

the Data Recovery link can have sub menus like "Data Recovery Process - Data Recovery Services - F.A.Q"

the Penetration Testing can have sub menus like "F.A.Q - Pentest Process - Pentest Services"

Here are links from website so you gather information:

-http://www.brelwick-disks.example/

-http://www.tolvenpathrescue.example/

-http://www.nimbrocore.example/

http://fentaloprestore.example/lp/disk-restore.aspx?src=web&ref=ZQPLx4TrmvaKDJ-wuHafk9RB2x
http://www.vqlt.example/
http://www.pembrastoneflow.example/data-recovery/
http://www.ytsarchiverescue.example/

thanks.

Target Market(s)

Any PC user

Industry/Entity Type

Data Recovery

Requirements
Must have
• - Language and geographic navigation
- Home page navigation
- Global navigation
- Breadcrumbs
Nice to have
• - Sliders
-Drop down navigation

```html
<!DOCTYPE html>
<html lang="en">
<head>
<meta charset="utf-8">
<title>Quorvane Consulting – Data Recovery</title>
<link href="https://fonts.googleapis.com/css2?family=Carlito:wght@400;700&family=Open+Sans:wght@400;600&family=Signika:wght@300;400;600&display=swap" rel="stylesheet">
<style>
:root{
  --red:#d8110f;
  --red-dark:#b20b0a;
  --black:#0b0b0b;
  --page:#f3f3f3;
  --panel:#fafafa;
  --ink:#222;
  --grey:#8a8a8a;
  --mid:#555;
  --navy:#3b3b5e;
  --bar:#e1e1e1;
}
*{box-sizing:border-box;margin:0;padding:0}
html,body{width:1178px;height:1200px;overflow:hidden}
body{background:var(--page);font-family:"Signika",sans-serif;color:var(--ink);position:relative}
.site{position:absolute;left:108px;top:27px;width:962px}
.locale-bar{height:23px;background:var(--black);color:#fff;font-size:12px;font-weight:600;display:flex;justify-content:flex-end;align-items:center;padding-right:26px;gap:12px;border-radius:3px 3px 0 0}
.locale-bar .lang{text-decoration:underline}
.header{height:120px;background:var(--panel);position:relative}
.brand{position:absolute;left:45px;top:46px;font-size:32px;font-weight:600;color:var(--ink);display:flex;align-items:center;gap:8px}
.brand .dot{width:12px;height:12px;background:var(--red);border-radius:50%}
.contact{position:absolute;right:22px;top:17px;text-align:right}
.contact .lead{font-size:17px;color:var(--navy)}
.contact .phone{font-size:20px;color:#333;margin-top:2px}
.contact .phone small{font-size:10px;color:#999;margin-left:8px}
.contact .quote{display:block;margin:4px 0 0 auto;width:186px;height:24px;border:1px solid #ddd;border-radius:3px;background:#f4f4f4;font-size:12px;font-weight:600;color:#444;line-height:22px;text-align:center}
.main-nav{height:55px;background:linear-gradient(#e0301a,#c81e0f);position:relative;color:#fff;font-weight:600;font-size:15px}
.main-nav a{position:absolute;top:18px;color:#fff;text-decoration:none}
.main-nav .active::after{content:"";position:absolute;left:50%;margin-left:-8px;top:37px;border:8px solid transparent;border-top-color:#c81e0f}
.search{position:absolute;left:741px;top:13px;width:201px;height:29px;background:#fff;border-radius:3px;font-size:11px;color:#aaa;padding:8px 12px;font-family:"Open Sans",sans-serif}
.search svg{position:absolute;right:8px;top:6px}
.sub-nav{height:33px;background:var(--black);position:relative;color:#fff;font-size:13px;font-weight:600}
.sub-nav a{position:absolute;top:9px;color:#fff;text-decoration:none}
.hero{height:364px;position:relative;overflow:hidden;background:linear-gradient(180deg,#eceae8 0%,#dedcda 55%,#8c8f96 88%,#5d6068 100%)}
.hero-photo{position:absolute;left:356px;top:30px;width:606px;height:334px;background:radial-gradient(ellipse at 55% 40%,#c9d3e6 0%,#a9b6cf 40%,#e8e8e8 75%,#f2f2f2 100%);clip-path:polygon(18% 100%,40% 40%,60% 2%,78% 30%,100% 70%,100% 100%)}
.hero h1{position:absolute;left:28px;top:100px;font-family:"Carlito",sans-serif;font-weight:700;font-size:41px;letter-spacing:-1.2px;color:var(--red);line-height:46px}
.hero h2{position:absolute;left:28px;top:146px;font-family:"Carlito",sans-serif;font-weight:700;font-size:41px;letter-spacing:-2px;color:#555;line-height:46px}
.hero p{position:absolute;left:28px;top:208px;width:420px;font-family:"Open Sans",sans-serif;font-size:14px;line-height:19px;color:#555}
.btn-light{position:absolute;left:27px;top:270px;width:150px;height:38px;background:linear-gradient(#fff,#eaeaea);border:1px solid #ccc;border-radius:3px;font-size:18px;color:#333;text-align:center;line-height:36px}
.services{height:152px;display:flex;background:linear-gradient(#e0100c,#c80b08);border-radius:0 0 4px 4px}
.service{flex:1;position:relative;padding:14px 0 0 19px;color:#fff;border-left:1px solid #b00806}
.service:first-child{border-left:none}
.service h3{font-size:22px;font-weight:400;line-height:26px}
.service h3 b{font-weight:600;display:block}
.service p{font-size:12.5px;font-weight:600;line-height:17px;margin-top:12px;width:210px}
.service .btn{position:absolute;left:19px;top:119px;width:82px;height:21px;background:#fff;border-radius:3px;color:#444;font-size:11px;text-align:center;line-height:21px}
.service .icon{position:absolute;right:36px;top:10px;width:50px;height:55px;background:linear-gradient(#d9d9d9,#8c8c8c);border-radius:4px}
.content{height:319px;background:var(--panel);position:relative}
.welcome{position:absolute;left:20px;top:38px;width:620px}
.welcome h2{font-size:25px;font-weight:400;color:#222}
.welcome p{font-family:"Open Sans",sans-serif;font-size:12.5px;line-height:19.6px;color:var(--grey);margin-top:19px}
.welcome h2+p{margin-top:17px}
.divider{position:absolute;left:656px;top:30px;width:1px;height:260px;background:#e4e4e4}
.why{position:absolute;left:678px;top:28px;width:270px}
.why h2{font-size:24px;font-weight:400;color:#222}
.why ul{list-style:none;margin-top:22px}
.why li{font-size:13px;letter-spacing:.6px;color:#666;line-height:19.6px;padding-left:28px;position:relative}
.why li::before{content:"";position:absolute;left:4px;top:6px;width:7px;height:7px;border-radius:50%;background:var(--red)}
.why .tag{color:var(--red);font-size:13px;letter-spacing:.3px;margin-top:20px;text-align:right}
.quick-links{height:40px;background:var(--bar);border-top:1px solid #ccc;border-bottom:1px solid #ccc;position:relative;font-weight:600;font-size:14px;color:#333}
.quick-links .title{position:absolute;left:23px;top:7px;font-size:20px;font-weight:400;letter-spacing:.5px}
.quick-links svg.home{position:absolute;left:139px;top:12px}
.quick-links svg.sep{position:absolute;left:172px;top:0}
.quick-links a{position:absolute;top:12px;color:#333;text-decoration:none}
.footer{position:relative;height:60px;font-size:12.5px;color:#333}
.footer .copy{position:absolute;left:19px;top:29px}
.footer nav{position:absolute;right:19px;top:29px}
.footer nav span{margin:0 9px}
</style>
</head>
<body>
<div class="site">
  <div class="locale-bar"><span class="lang">English</span><span>|</span><span>United States ▼</span></div>
  <header class="header">
    <div class="brand"><span>Quorvane</span><span class="dot"></span></div>
    <div class="contact">
      <div class="lead">Free Consultation Service</div>
      <div class="phone">555-014-2288<small>Or Call</small></div>
      <span class="quote">Request free Online Quote</span>
    </div>
  </header>
  <nav class="main-nav">
    <a style="left:18px">Home</a>
    <a style="left:122px">About</a>
    <a class="active" style="left:226px">Penetration Test</a>
    <a style="left:405px">Data Receovery</a>
    <a style="left:575px">Careers</a>
    <a style="left:678px">Search</a>
    <div class="search">Keyword
      <svg width="17" height="17" viewBox="0 0 17 17"><circle cx="10" cy="7" r="5.5" fill="none" stroke="#777" stroke-width="1.5"/><line x1="6" y1="11" x2="1.5" y2="15.5" stroke="#777" stroke-width="1.8"/></svg>
    </div>
  </nav>
  <nav class="sub-nav">
    <a style="left:20px">Data Recovery Process</a>
    <a style="left:206px">Data Recovery Services</a>
    <a style="left:395px">F.A.Q</a>
  </nav>
  <section class="hero">
    <div class="hero-photo" role="img" aria-label="Technician in a blue shirt inspecting an opened hard drive with a magnifying glass, tools spread on a white desk"></div>
    <h1>Dont Try it yourself</h1>
    <h2>If we can’t do. No one can do...</h2>
    <p>Le Lorem Ipsum est simplement du faux texte employé dans la composition et la mise en page avant impression.</p>
    <div class="btn-light">Read More</div>
  </section>
  <section class="services">
    <div class="service"><h3>Hard Disk<b>Recovery</b></h3><div class="icon" role="img" aria-label="Hard disk drive"></div><p>Le Lorem Ipsum est simplement du faux texte composition .</p><span class="btn">Read More</span></div>
    <div class="service"><h3>Raid<b>Recovery</b></h3><div class="icon" role="img" aria-label="RAID server rack" style="width:52px;background:linear-gradient(#6a7388,#2d3240)"></div><p>Le Lorem Ipsum est simplement du faux texte composition .</p><span class="btn">Read More</span></div>
    <div class="service"><h3 style="margin-top:3px">Flash<b>Drive Recovery</b></h3><div class="icon" role="img" aria-label="USB flash drive" style="right:10px;width:56px;background:linear-gradient(135deg,#555,#1b1b1b)"></div><p>Le Lorem Ipsum est simplement du faux texte composition .</p><span class="btn">Read More</span></div>
    <div class="service"><h3 style="margin-top:3px">Network<b>Securities</b></h3><div class="icon" role="img" aria-label="Blue padlock" style="right:20px;width:52px;background:linear-gradient(#7fc6f0,#1b7fc8)"></div><p>Le Lorem Ipsum est simplement du faux texte composition .</p><span class="btn">Read More</span></div>
  </section>
  <section class="content">
    <div class="welcome">
      <h2>Welcome to Quorvane Consulting</h2>
      <p>Lorem ipsum dolor sit amet, consectetuer adipiscing elit, sed diam nonummy nibh euismod tincidunt ut laoreet dolore magna aliquam erat volutpat. Ut wisi enim ad minim veniam, quis nostrud exerci tation ullam-corper suscipit lobortis nisl ut aliquip ex ea commodo consequat. Duis autem vel eum iriure dolor in hendrerit in vulputate velit esse molestie consequat,</p>
      <p>&nbsp;vel illum dolore eu feugiat nulla facilisis at vero eros et accumsan et iusto odio dignissim qui blandit praesent luptatum zzril delenit augue duis dolore te feugait nulla facilisi. Nam liber tempor cum soluta nobis eleifend option congue nihil imperdiet doming id quod mazim placerat facer possim assum.</p>
      <p>Typi non habent claritatem insitam; est usus legentis in iis qui facit eorum claritatem.</p>
    </div>
    <div class="divider"></div>
    <div class="why">
      <h2>Why Choose Quorvane</h2>
      <ul>
        <li>Reasonable pricing</li>
        <li>Entrust your data confidentiality</li>
        <li>Leading technology</li>
        <li>Immediate and prompt service</li>
        <li>Assured satisfaction</li>
        <li>Business trustworthiness</li>
        <li>Long term commitment</li>
        <li>Easy and hassle free process</li>
      </ul>
      <p class="tag">Because you need a RELIABLE vendor.</p>
    </div>
  </section>
  <nav class="quick-links">
    <span class="title">Quick Links</span>
    <svg class="home" width="16" height="15" viewBox="0 0 16 15"><path d="M8 1 L15 7.5 H13 V14 H9.5 V10 H6.5 V14 H3 V7.5 H1 Z" fill="#777"/></svg>
    <svg class="sep" width="14" height="40" viewBox="0 0 14 40"><polyline points="1,0 12,20 1,40" fill="none" stroke="#c4c4c4" stroke-width="1.2"/></svg>
    <a style="left:208px">Hard Drive</a>
    <a style="left:313px">Raid</a>
    <a style="left:378px">Mobile Phones</a>
    <a style="left:509px">MP3 Players</a>
    <a style="left:623px">Digital Cameras</a>
    <a style="left:760px">Tablets</a>
    <a style="left:843px">Memory Cards</a>
  </nav>
  <footer class="footer">
    <div class="copy">Copyright 2012 Website Name. All Rights Reserved.</div>
    <nav>Home<span>|</span>About<span>|</span>Penetration Test<span>|</span>Data Receovery<span>|</span>Careers</nav>
  </footer>
</div>
</body>
</html>
```